Slider needed for Database Documentation Topic

We need a slider to promote a content area of a web site. I'm listing this as a poster because the posters I have seen on FrameHarbor portfolios most closely resemble the combination or art and text I am looking for.
The content area we are promoting with this graphic will clarify the design and use of a complicated database. The title of the content area is "The Kindled VQ Database" and the banner should use that title.
To 'illuminate' something means to cast light on it, and this content area will help shed light on a complicated thing – the content will use diagrams, text, and examples to clarify the database. Another meaning is that an illuminated manuscript is a manuscript brought to life with pictures, and in a way that is also what this content area will do.
One idea for the slider might be a light bulb, lamp, candle or flashlight lighting up the words "VQ Database". Another idea would be the type of illustration you see if you search for "Illuminated manuscript"
But I'm not committed to any particular idea - in the past I have been pleased to see ideas that are different than my own but accomplish the same thing, so please feel free to use your judgement or ask any questions.
In addition to the title (The Kindled VQ Database) the graphic should allow room for three smaller lines of text – the three bullet items below:
- Guide to understanding the VQ database
- Data sources, uses and relationships explained with illustrations
- New content! Customers
The last bullet item will change as the content is added.
Some particulars ...
SIZE - 600 high x 1200 wide pixels
PHOTOS vs ILLUSTRATION - I am open to either one.

```html
<!DOCTYPE html>
<html lang="en">
<head>
<meta charset="utf-8">
<title>The Kindled VQ Database</title>
<link rel="stylesheet" href="https://fonts.googleapis.com/css2?family=UnifrakturCook:wght@700&family=UnifrakturMaguntia&display=swap">
<style>
  :root {
    --ink-dark: #0e2429;
    --ink-slate: #3a5058;
    --glow-white: #ffffff;
    --teal-deep: #0d3540;
    --teal-mid: #3f8a9a;
    --teal-pale: #bfe8ef;
    --shadow-navy: #08121a;
    --flare-rose: rgba(230, 120, 170, 0.45);
  }
  * { margin: 0; padding: 0; box-sizing: border-box; }
  html, body {
    width: 1200px;
    height: 600px;
    overflow: hidden;
    background: #ffffff;
  }
  .slider {
    position: relative;
    width: 1200px;
    height: 600px;
    overflow: hidden;
  }
  .backdrop-art {
    position: absolute;
    inset: 0;
    background:
      radial-gradient(circle at 300px 120px, var(--flare-rose) 0, transparent 110px),
      radial-gradient(ellipse 260px 200px at 600px 300px, var(--glow-white) 0, rgba(255,255,255,0.85) 55%, transparent 100%),
      linear-gradient(135deg, var(--shadow-navy) 0%, var(--teal-deep) 14%, transparent 32%),
      linear-gradient(225deg, var(--shadow-navy) 0%, var(--teal-deep) 14%, transparent 32%),
      linear-gradient(45deg, var(--shadow-navy) 0%, var(--teal-deep) 12%, transparent 30%),
      linear-gradient(315deg, #1c4f58 0%, var(--teal-mid) 12%, transparent 30%),
      linear-gradient(90deg, var(--teal-pale) 0%, #ffffff 40%, #ffffff 60%, var(--teal-pale) 100%);
  }
  .banner-title {
    position: absolute;
    top: 128px;
    left: 0;
    width: 1200px;
    text-align: center;
    font-family: "UnifrakturMaguntia", "UnifrakturCook", serif;
    font-size: 66px;
    font-weight: 400;
    letter-spacing: 3px;
    color: var(--ink-dark);
    text-shadow:
      2px 2px 0 var(--glow-white), -2px -2px 0 var(--glow-white),
      2px -2px 0 var(--glow-white), -2px 2px 0 var(--glow-white),
      4px 5px 6px rgba(0,0,0,0.45);
  }
  .feature-list {
    position: absolute;
    top: 228px;
    left: 268px;
    list-style: none;
    font-family: "UnifrakturCook", "UnifrakturMaguntia", serif;
    font-weight: 700;
    font-size: 29px;
    letter-spacing: 2px;
    line-height: 42px;
    color: var(--ink-slate);
    text-shadow: 2px 2px 3px rgba(255,255,255,0.9), 3px 3px 4px rgba(0,0,0,0.25);
  }
  .feature-item {
    position: relative;
    padding-left: 52px;
    margin-bottom: 14px;
    max-width: 800px;
  }
  .feature-item:last-child { margin-top: -14px; }
  .feature-bullet {
    position: absolute;
    left: 4px;
    top: 8px;
    width: 34px;
    height: 30px;
    border-radius: 6px;
    background: linear-gradient(180deg, #4d6670, var(--ink-slate));
  }
</style>
</head>
<body>
  <main class="slider">
    <div class="backdrop-art" role="img" aria-label="Lit view upward between tall teal and dark stone blocks with a bright white cross of light in the centre"></div>

    <h1 class="banner-title">The Kindled VQ Database</h1>

    <ul class="feature-list">
      <li class="feature-item"><span class="feature-bullet" role="img" aria-label="fleur-de-lis bullet"></span>Guide to understanding the VQ database.</li>
      <li class="feature-item"><span class="feature-bullet" role="img" aria-label="fleur-de-lis bullet"></span>Data sources, uses and relationships explained with illustrations.</li>
      <li class="feature-item"><span class="feature-bullet" role="img" aria-label="fleur-de-lis bullet"></span>New content! Customers.</li>
    </ul>
  </main>
</body>
</html>
```